Asphalt Paving Specialists Business Cards

Our company is TREVIN ASPHALT. We need a business cards two of our asphalt paving team members. We're asphalt specialists.
I need two made up please. The details on the front of the each business card i would like please is as follows.
Address is 87 Marrowby St, Clontarf, QLD, 4019.

Company Director
Gordon Pelliway
gord@trevinpave.com.au
04 58 736 042
www.trevinpave.com.au

Supervisor
Curtis Vonnegard
curtis@trevinpave.com.au
0462 873 105
www.trevinpave.com.au

We do all aspects of Asphalt Paving. Specific Services include - Driveways, Carparks & sub-divisions. All Roads. Repairs and Maintenance.

We provide free quotes!

I dont have a certain way i want them to look so im open to all designs :)

** I have uploaded our logo for the TREVIN ASPHALT. HOWEVER, CAN YOU PLEASE GET RID OF THE ( PTY LTD )

Thank you
Renata Fulch
TREVIN ASPHALT

Target Market(s)

Home owners and Business Owners

Contact Information for Business Card

Asphalt Paving Specialists. All aspects of Asphalt. Residential, Commercial & Industrial. Based in Brisbane.

Font styles to use
Sans Serif

Colors

Designer to choose colors to be used in the design.

Requirements
Nice to have
• maybe an image of a driveway? or Asphalt?

```html
<!DOCTYPE html>
<html lang="en">
<head>
<meta charset="utf-8">
<title>Curtis Vonnegard – Supervisor – Trevin Asphalt</title>
<link rel="stylesheet" href="https://fonts.googleapis.com/css2?family=Archivo:wdth,wght@62..125,400..900&display=swap">
<style>
  :root {
    --asphalt-dark: #2e2d2d;
    --asphalt-mid: #3b3a3a;
    --asphalt-light: #474545;
    --ink-light: #f0f0f0;
    --ink-soft: #e4e4e4;
  }
  * { margin: 0; padding: 0; box-sizing: border-box; }
  html, body {
    width: 1200px;
    height: 667px;
    overflow: hidden;
    background: var(--asphalt-dark);
  }
  .card {
    position: relative;
    width: 1200px;
    height: 667px;
    overflow: hidden;
    font-family: "Archivo", Arial, sans-serif;
    color: var(--ink-light);
  }
  .card__surface {
    position: absolute;
    inset: 0;
    background:
      radial-gradient(ellipse at 25% 20%, var(--asphalt-light) 0%, transparent 60%),
      radial-gradient(ellipse at 85% 85%, var(--asphalt-mid) 0%, transparent 65%),
      linear-gradient(160deg, var(--asphalt-mid) 0%, var(--asphalt-dark) 100%);
  }
  .role {
    position: absolute;
    left: 77px;
    top: 88px;
    font-size: 39px;
    font-weight: 400;
    letter-spacing: 2px;
    line-height: 1;
    color: var(--ink-soft);
  }
  .name {
    position: absolute;
    left: 74px;
    top: 142px;
    font-size: 110px;
    font-weight: 900;
    font-stretch: 84%;
    line-height: 1;
    letter-spacing: 0.5px;
    white-space: nowrap;
  }
  .contact {
    position: absolute;
    right: 88px;
    text-align: right;
    white-space: nowrap;
    line-height: 1;
  }
  .contact--email {
    top: 372px;
    font-size: 43px;
    font-weight: 800;
    font-stretch: 90%;
    letter-spacing: 1.5px;
  }
  .contact--phone {
    top: 478px;
    font-size: 45px;
    font-weight: 400;
    letter-spacing: 8px;
    display: flex;
    align-items: center;
    gap: 12px;
    margin-right: -8px;
  }
  .contact--phone .phone-icon { width: 48px; height: 48px; flex: none; }
  .contact--web {
    top: 536px;
    font-size: 43px;
    font-weight: 400;
    letter-spacing: 2.5px;
  }
</style>
</head>
<body>
  <main class="card">
    <div class="card__surface" role="img" aria-label="Close-up photograph of a fresh asphalt surface"></div>

    <p class="role">Supervisor</p>
    <h1 class="name">Curtis Vonnegard</h1>

    <p class="contact contact--email">curtis@trevinpave.com.au</p>

    <p class="contact contact--phone">
      <svg class="phone-icon" viewBox="0 0 50 50" aria-hidden="true">
        <circle cx="25" cy="25" r="22" fill="none" stroke="var(--ink-light)" stroke-width="2.5"/>
        <path d="M17 14c1.5-1 3-1 3.8.4l2.3 4c.6 1.1.2 2.2-.8 2.9l-1.6 1.1c.9 2.6 3 4.9 5.5 6.2l1.2-1.5c.8-.9 2-1.2 3-.6l3.9 2.4c1.3.8 1.3 2.3.3 3.7l-1.3 1.8c-1 1.3-2.9 1.8-4.7 1.1C21.8 33.4 15.5 26.8 14 19.7c-.4-1.8.2-3.6 1.5-4.7z" fill="var(--ink-light)"/>
      </svg>
      <span>04 62 873 105</span>
    </p>

    <p class="contact contact--web">www.trevinpave.com.au</p>
  </main>
</body>
</html>
```